Web Design Project - grocery store

A small grocery store in Germany selling food and cloths wants his own web site. They want to set up a new webpage as the old isn't up2date anymore. The page shall cover the consumer usecases: I as a consumer wants to INFORM me, ORDER stuff, check COUPONs, ADVERTISE, LIKE the stuff.
* INFORM: The page shall show the current offers for food (basic, organic, whole, butcher, bakery) and cloths (different brands for men, women and kids). There then the latest news and offers are placed.
* ORDER: The page shall list a set of affiliates where the consumer can order stuff (and if available collect in the store). These are basically German affiliates like Lunavo, PRAVI foto shop or some local insurance services. The page shall show their content and in case the consumer orders then interact with their system having an merchant ID so that the purchase can be booked in the merchant account for its bonus payments. Also, it could be that the page just present the link to the affiliate page and the consumer then interact there.
* COUPONs: The page shall connect to a coupon service and present the current coupons available. For purchasing the consumer uses a link and the values are booked then in the external service's system.
* ADVERTISE: The page shall offer a function where the consumer can place an offer. Also, there are some Consumer2Consumer pages available where the data could be grabbed and presented. Would be then a web service to integrate.
* LIKE: The page shall list the Chatterloop interaction there. The consumer can like and place comments at the wall.

```html
<!DOCTYPE html>
<html lang="en">
<head>
<meta charset="utf-8">
<title>Halvorn – Grocery Store</title>
<link href="https://fonts.googleapis.com/css2?family=Ubuntu:wght@400;500&family=Arimo&display=swap" rel="stylesheet">
<style>
:root{
  --bg:#262b2f;
  --bg-light:#3d4247;
  --footer:#121416;
  --white:#ffffff;
  --cyan:#19d6ee;
  --cyan-deep:#0aa3d4;
  --brand:#1d8fc4;
  --banner:#d5f3fa;
  --heading-blue:#1b7ea6;
  --button:#1579a8;
  --tabbar:#5c6268;
  --text:#eef1f3;
  --muted:#c9cfd4;
  --divider:#d9dde0;
}
*{margin:0;padding:0;box-sizing:border-box}
html,body{width:950px;height:1200px;overflow:hidden}
body{position:relative;font-family:"Ubuntu",sans-serif;color:var(--text);
  background:radial-gradient(ellipse 600px 700px at 475px 420px,var(--bg-light),var(--bg) 80%)}
.abs{position:absolute}
/* header */
.header{left:0;top:0;width:950px;height:113px;background:var(--white);display:flex}
.logo-area{width:308px;height:113px;background:linear-gradient(90deg,#fff,#eef2f5 60%,#fff);position:relative}
.logo{position:absolute;left:50px;top:30px;font-size:38px;font-weight:500;color:var(--brand)}
.nav{display:flex}
.nav a{width:107px;height:113px;display:flex;align-items:center;justify-content:center;
  color:#222;text-decoration:none;font-size:15px;border-left:1px solid var(--divider);padding-bottom:0}
.nav a.active{background:linear-gradient(#00f0fa,#0aa6d8);color:#123;border:none}
.social-badge{left:891px;top:88px;width:60px;height:60px;border-radius:50%;background:var(--brand);
  border:3px solid #fff;color:#fff;font-size:9px;display:flex;align-items:center;justify-content:center}
/* utility bar */
.utility{top:136px;font-size:12px;color:var(--text);display:flex;align-items:center;gap:12px}
.utility .sep{color:var(--muted)}
/* banner */
.banner{left:41px;top:175px;width:867px;height:281px;background:var(--banner);border:2px solid #fff;
  border-radius:8px;box-shadow:0 6px 14px rgba(0,0,0,.5)}
.banner-photo{left:80px;top:20px;width:370px;height:250px;border-radius:6px;
  background:radial-gradient(circle at 60% 40%,#e8f5f8,#b9dbe4 55%,var(--banner) 75%)}
.banner-title{left:490px;top:66px;font-size:38px;color:var(--heading-blue);letter-spacing:1px}
.banner-text{left:490px;top:127px;width:320px;font-size:15px;line-height:21px;color:#222}
.btn{left:711px;top:180px;width:80px;height:25px;background:var(--button);color:#fff;font-size:12px;
  display:flex;align-items:center;justify-content:center}
.dots{left:664px;top:244px;display:flex;gap:17px}
.dots span{width:12px;height:12px;border-radius:50%;background:#1f2a30}
.dots span.on{background:var(--button)}
.arrow{top:300px}
/* welcome */
.welcome-title{left:59px;top:488px;font-size:21px}
.welcome-title em{font-style:normal;color:var(--cyan);font-size:25px}
.welcome-text{left:59px;top:535px;width:835px;font-size:12.5px;line-height:21px}
.more-link{left:833px;top:606px;font-size:12.5px;color:var(--cyan);text-decoration:underline}
/* tabs */
.tabs{left:43px;top:662px;width:866px;height:56px;background:var(--tabbar);border-radius:6px}
.tab{top:17px;font-size:18px;display:flex;align-items:center;gap:16px}
.tab i{width:12px;height:12px;border-radius:50%;background:#fff;display:block}
.tab i.ring,.section-title i{width:18px;height:18px;background:var(--cyan-deep);border:3px solid #dfe9ee}
/* section */
.section-title{left:59px;top:742px;font-size:18px;display:flex;align-items:center;gap:17px}
.section-title i{border-radius:50%;display:block}
.section-text{left:94px;top:783px;width:518px;font-family:"Arimo",sans-serif;font-size:11.3px;line-height:21px}
.section-photo{left:657px;top:762px;width:225px;height:133px;border:2px solid #dff5fb;border-radius:6px;
  background:radial-gradient(ellipse at 50% 50%,#f1e6dc,#b7aaa2 55%,#6f6b6a)}
.items{top:937px;font-size:12px;display:flex;align-items:center;gap:13px}
.items i{width:8px;height:8px;border-radius:50%;background:#fff;display:block}
.thumb{top:970px;width:135px;height:75px;border-radius:5px}
/* footer */
.footer{left:0;top:1077px;width:950px;height:123px;background:var(--footer)}
.footer-nav{top:1105px;left:0;width:950px;text-align:center;font-size:11px;color:var(--text)}
.footer-nav span{color:var(--muted);margin:0 6px}
.copyright{left:30px;top:1154px;font-size:11px}
.connect{right:30px;top:1152px;font-size:11px;display:flex;gap:10px;align-items:center}
.connect b{font-weight:400;color:var(--cyan)}
</style>
</head>
<body>
<header class="abs header">
  <div class="logo-area"><div class="logo">Halvorn</div></div>
  <nav class="nav">
    <a class="active" href="#">Home</a><a href="#">Inform</a><a href="#">Order</a><a href="#">Coupons</a><a href="#">Advertise</a><a href="#">Contact us</a>
  </nav>
</header>
<div class="abs social-badge">Chatterloop</div>

<div class="abs utility" style="left:27px">
  <svg width="20" height="18" viewBox="0 0 20 18"><path d="M1 2h3l2 9h10l2-7H6" fill="none" stroke="#fff" stroke-width="2"/><circle cx="8" cy="15" r="1.8" fill="#fff"/><circle cx="15" cy="15" r="1.8" fill="#fff"/></svg>
  <span>My Cart (0) items</span><span class="sep">|</span><span>Wish List</span><span class="sep">|</span><span>My Account</span>
</div>
<div class="abs utility" style="left:778px"><span>Log in</span><span class="sep">|</span><span>Register</span></div>

<section class="abs banner">
  <div class="abs banner-photo" role="img" aria-label="Packaged chicken breast fillets beside a frozen chicken roll"></div>
  <h1 class="abs banner-title" style="font-weight:400">FROZEN CHICKEN</h1>
  <p class="abs banner-text">Lorem ipusem Tavrin are also reproduced in their exact original form.</p>
  <a class="abs btn">View more</a>
  <div class="abs dots"><span class="on"></span><span></span><span></span><span></span><span></span></div>
</section>
<svg class="abs arrow" style="left:28px" width="26" height="32" viewBox="0 0 26 32"><path d="M22 2L4 16l18 14" fill="none" stroke="#e8ecef" stroke-width="6" stroke-linejoin="round"/></svg>
<svg class="abs arrow" style="left:896px" width="26" height="32" viewBox="0 0 26 32"><path d="M4 2l18 14L4 30" fill="none" stroke="#e8ecef" stroke-width="6" stroke-linejoin="round"/></svg>

<h2 class="abs welcome-title" style="font-weight:400">Welcome to <em>Halvorn</em></h2>
<p class="abs welcome-text">Contrary to popular belief, Lorem Ipsum is not simply random text. It has roots in a piece of classical Latin literature from 45 BC, making it over 2000 years old. Orvel Tamsin, a Latin professor at Brookfield College in Cordavia, looked up one of the more obscure Latin words, consectetur, from a Lorem Ipsum passage, and going through the cites of the word in classical literature discovered the undoubtable source.</p>
<a class="abs more-link">View more</a>

<div class="abs tabs">
  <div class="abs tab" style="left:30px"><i class="ring" style="border-radius:50%"></i>Frozen chicken</div>
  <div class="abs tab" style="left:229px"><i></i>Mutton packets</div>
  <div class="abs tab" style="left:443px"><i></i>Cakes</div>
  <div class="abs tab" style="left:587px"><i></i>Pastries</div>
  <div class="abs tab" style="left:740px"><i></i>Cloths</div>
</div>

<h3 class="abs section-title" style="font-weight:400"><i></i>Frozen chicken</h3>
<p class="abs section-text">It is a long established fact that a reader will be distracted by the readable content of a page when looking at its layout. The point of using Lorem Ipsum is that it has a more-or-less normal distribution of letters, as opposed to using 'Content here, content here', making it look like readable English. Many desktop publishing packages and web page editors now use Lorem Ipsum as their default model text, and a search for 'lorem ipsum' will uncover many web sites still in their infancy. Various versions have evolved over the years, sometimes by accident, sometimes on purpose.</p>
<div class="abs section-photo" role="img" aria-label="Whole raw chicken"></div>

<div class="abs items" style="left:96px"><i></i>Chicken Wing Tips</div>
<div class="abs items" style="left:254px"><i></i>Supreme pices</div>
<div class="abs items" style="left:409px"><i></i>Chicken Paws</div>
<div class="abs items" style="left:542px"><i></i>Chicken Breast Fillets</div>
<div class="abs items" style="left:700px"><i></i>Chicken Dummbels</div>

<div class="abs thumb" style="left:88px;background:linear-gradient(90deg,#3a2a2a,#e8d4d0 45%,#2a2020)" role="img" aria-label="Raw chicken wing tips"></div>
<div class="abs thumb" style="left:239px;background:radial-gradient(ellipse at 50% 50%,#7a4a3a,#111 60%)" role="img" aria-label="Chicken paws"></div>
<div class="abs thumb" style="left:392px;background:linear-gradient(135deg,#f2e8e0,#c9734a 45%,#6a8a3a 70%,#eee)" role="img" aria-label="Plated chicken dish with vegetables"></div>
<div class="abs thumb" style="left:545px;background:radial-gradient(ellipse at 50% 55%,#e9c4b8,#fff 65%)" role="img" aria-label="Raw chicken breast fillets"></div>
<div class="abs thumb" style="left:698px;background:radial-gradient(ellipse at 50% 50%,#c98a45,#fff6ea 65%)" role="img" aria-label="Chicken drumsticks"></div>

<footer class="abs footer"></footer>
<div class="abs footer-nav">Home<span>|</span>Inform<span>|</span>Order<span>|</span>Coupons<span>|</span>Advertise<span>|</span>Contact us<span>|</span>Sitemap</div>
<div class="abs copyright">Copyright © 2011 www.halvorn.com &nbsp;&nbsp; All rights reserved</div>
<div class="abs connect">Connect with us : <b>Chatterloop</b><b>Chirpline</b><b>Postwell</b><b>Workmesh</b><b>Searchly</b></div>
</body>
</html>
```